Kestrim LLC, needs a web page no more than 5 pages (for now)

Kestrim is a general contractor. Our services include general contracting, design-build construction, disaster recovery and environmental remediation. Our main clients are KZE, HJ, State and Local Gov't Agencies, Hospitals and Schools. Kestrim is also a SDVOSB.

```html
<!DOCTYPE html>
<html lang="en">
<head>
<meta charset="utf-8">
<title>Kestrim LLC – General Contractor</title>
<link href="https://fonts.googleapis.com/css2?family=Poppins:wght@400;500;600;700;800&display=swap" rel="stylesheet">
<style>
:root{
  --gold:#c9a13f;
  --gold-light:#e8cd6a;
  --gold-dark:#a87d25;
  --gold-grad:linear-gradient(90deg,#b88a2c 0%,#e4c860 45%,#c99a35 100%);
  --ink:#0e0e0e;
  --ink-2:#1b1b1b;
  --bar:#2b2b2b;
  --text:#1a1a1a;
  --muted:#5a5a5a;
  --line:#e6e6e6;
  --white:#ffffff;
}
*{box-sizing:border-box;margin:0;padding:0}
html,body{width:1200px;height:4680px;overflow:hidden}
body{font-family:'Poppins',sans-serif;color:var(--text);background:var(--white);position:relative}
.abs{position:absolute}
section,header,footer{position:absolute;left:0;width:1200px}

/* top bar */
.topbar{top:0;height:33px;background:var(--bar);color:#ddd;font-size:10px;display:flex;align-items:center;padding:0 104px;z-index:5}
.topbar .item{display:flex;align-items:center;gap:6px;padding-right:22px;margin-right:22px;border-right:1px solid #555}
.topbar .item:last-of-type{border:none}
.topbar .follow{margin-left:auto;display:flex;align-items:center;gap:10px}
.topbar .soc{width:10px;height:10px;background:#ddd;border-radius:2px}
.ico{width:10px;height:10px;fill:var(--gold);flex:none}

/* hero */
.hero{top:33px;height:807px;background:linear-gradient(180deg,#151515 0%,#0b0b0b 55%,#222 100%);overflow:hidden}
.hero-bg{left:0;top:0;width:1200px;height:640px;background:linear-gradient(180deg,#1e1e1e 0%,#111 50%,#2a2a2a 100%)}
.brand{display:flex;align-items:center;gap:8px;color:var(--white);font-weight:700;font-size:20px;letter-spacing:.5px}
.brand .mark{width:14px;height:14px;border-radius:50%;background:var(--gold)}
.nav{top:34px;left:104px;right:104px;height:40px;display:flex;align-items:center;z-index:4}
.nav ul{list-style:none;display:flex;gap:32px;margin-left:auto;margin-right:32px;color:var(--white);font-size:10px;font-weight:600}
.btn-gold{background:var(--gold-grad);color:var(--white);font-weight:600;font-size:9px;border-radius:22px;display:inline-flex;align-items:center;justify-content:center;text-transform:uppercase}
.nav .btn-gold{width:148px;height:40px}
.worker{left:640px;top:150px;width:300px;height:657px;background:linear-gradient(180deg,#d9b03a 0%,#c98440 28%,#f08a2a 55%,#4a3a2a 100%);border-radius:130px 130px 0 0;z-index:1}
.hero h1{left:172px;top:118px;font-size:80px;line-height:88px;font-weight:700;color:var(--white);letter-spacing:-1.5px;z-index:3}
.hero .lead{left:176px;top:310px;width:495px;font-size:13px;line-height:20px;color:#e5e5e5;z-index:3}
.hero .cta{left:177px;top:373px;display:flex;gap:14px;align-items:center;z-index:3}
.hero .cta .btn-gold{width:165px;height:42px}
.play{width:42px;height:42px;border-radius:50%;background:#3a3a3a;display:flex;align-items:center;justify-content:center}
.stats{left:176px;top:476px;display:flex;gap:58px;color:var(--white);z-index:3}
.stat b{display:block;font-size:44px;font-weight:700;line-height:50px}
.stat b span{color:var(--gold)}
.stat small{font-size:11px}
.quote-band{left:0;top:640px;width:1200px;height:167px}
.quote-txt{left:103px;top:704px;font-size:25px;font-weight:700;color:var(--white);border-bottom:2px solid var(--white);line-height:34px;z-index:3;white-space:nowrap}
.quote-go{left:1040px;top:703px;width:56px;height:56px;border-radius:50%;background:rgba(255,255,255,.25);display:flex;align-items:center;justify-content:center;z-index:3}

/* about */
.about{top:840px;height:880px}
.about .para{left:191px;top:108px;width:400px;font-size:12px;line-height:19px;color:var(--muted);text-align:right}
.about .link{left:508px;top:237px;font-size:9px;font-weight:700;color:var(--gold);display:flex;align-items:center;gap:8px}
.dot-gold{width:14px;height:14px;border-radius:50%;background:var(--gold)}
.about h2{left:669px;top:107px;font-size:38px;line-height:45px;font-weight:700}
.team-photo{left:191px;top:333px;width:818px;height:354px;border-radius:26px;background:linear-gradient(120deg,#c8cdd2 0%,#e6a14a 40%,#f0c23a 60%,#8aa0b4 100%)}
.features{left:191px;top:742px;display:flex;gap:92px}
.feature{width:210px}
.feature .head{display:flex;align-items:center;gap:14px}
.feature .badge{width:62px;height:62px;border-radius:50%;background:var(--gold-grad);flex:none}
.feature h3{font-size:18px;line-height:23px;font-weight:700}
.feature p{margin-top:20px;font-size:11.5px;line-height:19px;color:var(--muted)}

/* services */
.services{top:1787px;height:653px}
.services h2{left:103px;top:120px;font-size:40px;line-height:46px;font-weight:700;color:var(--white)}
.services .sub{left:103px;top:233px;font-size:11.5px;color:#cfcfcf}
.svc-list{left:104px;top:282px;width:450px;list-style:none}
.svc-list li{color:var(--white);font-size:24px;font-weight:700;padding:12px 0 14px;border-bottom:1px solid #333}
.svc-list li:last-child{border:none}
.svc-list li.active{color:var(--gold)}
.svc-list li small{display:block;font-size:11px;font-weight:400;color:#bbb;margin-top:4px}
.svc-photo{left:642px;top:227px;width:452px;height:313px;border-radius:22px;background:linear-gradient(135deg,#4a6a9a 0%,#d9d9d9 45%,#e0c040 70%,#7a6040 100%)}
.pill{left:755px;top:127px;width:338px;height:56px;border-radius:30px;background:rgba(255,255,255,.12);display:flex;align-items:center;padding-left:110px;color:var(--white);font-size:10px;font-weight:700;line-height:14px}
.pill .avatar{position:absolute;left:5px;top:-20px;width:76px;height:76px;border-radius:38px 38px 30px 30px;background:linear-gradient(180deg,#e4c040,#e87d2a)}
.pill .dot-gold{position:absolute;right:14px;top:13px;width:30px;height:30px}

/* industries */
.industries{top:2440px;height:872px}
.industries h2{left:178px;top:85px;font-size:38px;line-height:46px;font-weight:700}
.industries .intro{left:711px;top:92px;width:330px;font-size:11.5px;line-height:19px;color:var(--muted)}
.industries .link{left:711px;top:168px;font-size:9px;font-weight:700;color:var(--gold);display:flex;align-items:center;gap:8px}
.tile{border-radius:12px;overflow:hidden}
.t1{left:187px;top:251px;width:440px;height:249px;background:linear-gradient(180deg,#b8c4d0 0%,#5a6a5a 55%,#2a3a2a 100%)}
.t2{left:640px;top:251px;width:373px;height:249px;background:linear-gradient(180deg,#c7d6e4 0%,#c8b294 55%,#6a7a5a 100%)}
.t3{left:187px;top:509px;width:289px;height:247px;background:linear-gradient(160deg,#d8dde3 0%,#8a9a8a 60%,#4a5a4a 100%)}
.t4{left:487px;top:509px;width:526px;height:247px;background:linear-gradient(180deg,#aec5dc 0%,#a89470 55%,#3e6a2e 100%)}
.t1 .cap{position:absolute;left:32px;bottom:22px;color:var(--white)}
.t1 .cap small{display:block;color:var(--gold-light);font-size:11px;font-weight:600}
.t1 .cap b{font-size:23px;font-weight:700}
.t1 .go{position:absolute;right:30px;bottom:28px;width:42px;height:42px;border-radius:50%;background:var(--gold-grad)}

/* values band */
.values{top:3312px;height:288px}
.value{position:absolute;top:74px;width:220px;text-align:center;color:var(--white);font-size:18px;font-weight:700;line-height:24px}
.value .circ{width:84px;height:84px;border-radius:50%;background:var(--white);margin:0 auto 30px;display:flex;align-items:center;justify-content:center}
.value .circ span{width:40px;height:40px;border-radius:50%;border:3px solid var(--gold)}

/* contact */
.contact{top:3600px;height:636px}
.c-card{left:191px;top:118px;width:265px;height:394px;background:var(--ink);border-radius:10px;color:var(--white);padding:50px 26px}
.c-card h2{font-size:34px;line-height:38px;font-weight:700;letter-spacing:-.5px}
.c-card .tag{margin-top:16px;color:var(--gold);font-size:10px;font-weight:600}
.c-card p{margin-top:12px;font-size:9.5px;line-height:15px;color:#ccc;padding-bottom:22px;border-bottom:1px solid #333}
.c-card ul{list-style:none;margin-top:24px;font-size:10.5px}
.c-card li{display:flex;align-items:center;gap:10px;margin-bottom:12px}
.form{left:480px;top:118px;width:529px;height:394px;border:1px solid var(--line);border-radius:10px;padding:48px 28px}
.form h3{font-size:18px;line-height:24px;font-weight:700}
.form h3 span{color:var(--gold)}
.fields{margin-top:26px;display:grid;grid-template-columns:1fr 1fr;gap:14px 8px}
.field{height:36px;border:1px solid var(--line);border-radius:18px;background:#f7f7f7;font-size:10px;color:#999;padding:0 26px;display:flex;align-items:center}
.field.full{grid-column:1/3;height:96px;border-radius:10px;align-items:flex-start;padding-top:14px}
.form .btn-gold{margin-top:22px;width:166px;height:42px}

/* footer */
.footer{top:4236px;height:444px;background:linear-gradient(180deg,#151515,#0a0a0a)}
.footer .brand{position:absolute;left:104px;top:94px}
.footer .tag{left:104px;top:154px;color:var(--white);font-size:18px;font-weight:700}
.footer .about-f{left:104px;top:193px;width:300px;font-size:11.5px;line-height:19px;color:#bbb}
.f-soc{left:104px;top:256px;display:flex;gap:12px}
.f-soc span{width:41px;height:41px;border-radius:50%;border:1px solid #555;display:flex;align-items:center;justify-content:center}
.f-soc span i{width:14px;height:14px;background:#ddd;border-radius:3px}
.vline{left:465px;top:0;width:1px;height:410px;background:#333}
.hline{left:465px;top:220px;width:735px;height:1px;background:#333}
.footer .ready{left:533px;top:110px;font-size:26px;line-height:32px;font-weight:700;color:var(--white)}
.footer .btn-gold{position:absolute;left:929px;top:124px;width:164px;height:40px}
.cols{left:533px;top:232px;display:flex}
.col{width:148px;color:var(--white)}
.col h4{font-size:14px;font-weight:700;margin-bottom:14px}
.col li{list-style:none;font-size:10px;color:#ccc;line-height:19px}
.bottom{left:104px;right:104px;top:408px;height:36px;display:flex;justify-content:space-between;align-items:center;font-size:10px;color:#bbb;border-top:1px solid #333}
</style>
</head>
<body>

<header class="topbar">
  <div class="item"><svg class="ico" viewBox="0 0 10 10"><path d="M5 0a3.5 3.5 0 0 0-3.5 3.5C1.5 6 5 10 5 10s3.5-4 3.5-6.5A3.5 3.5 0 0 0 5 0zm0 5a1.5 1.5 0 1 1 0-3 1.5 1.5 0 0 1 0 3z"/></svg>123 Main Street, City, Country</div>
  <div class="item"><svg class="ico" viewBox="0 0 10 10"><path d="M2 0l2 2-1 1.5a6 6 0 0 0 3.5 3.5L8 6l2 2-1.5 2C4 10 0 6 0 1.5z"/></svg>+1 (234) 567 890</div>
  <div class="item"><svg class="ico" viewBox="0 0 10 10"><path d="M0 2h10v6H0z"/></svg>info@kestrim.com</div>
  <div class="follow">Follow Us On: <span class="soc"></span><span class="soc"></span><span class="soc"></span><span class="soc"></span></div>
</header>

<section class="hero">
  <div class="abs hero-bg" role="img" aria-label="Dusk construction site with cranes and steel framing"></div>
  <nav class="abs nav">
    <div class="brand"><span class="mark"></span>Kestrim</div>
    <ul><li>HOME</li><li>ABOUT US</li><li>SERVICES</li><li>CLIENTS</li><li>PROJECTS</li><li>CONTACT</li></ul>
    <span class="btn-gold">Get A Free Quote</span>
  </nav>
  <svg class="abs quote-band" viewBox="0 0 1200 167" preserveAspectRatio="none">
    <defs><linearGradient id="gb" x1="0" x2="1"><stop offset="0" stop-color="#b88a2c"/><stop offset=".5" stop-color="#d9b64e"/><stop offset="1" stop-color="#c29433"/></linearGradient></defs>
    <path d="M0 0H320C345 0 350 20 375 20H1200V167H0z" fill="url(#gb)"/>
  </svg>
  <div class="abs worker" role="img" aria-label="Contractor in hard hat and safety vest holding a laptop"></div>
  <h1 class="abs">Building Strong<br>Foundations</h1>
  <p class="abs lead">Kestrim is a trusted SDVOSB general contractor specializing in government, healthcare, and education infrastructure.</p>
  <div class="abs cta"><span class="btn-gold">View Our Project</span><span class="play"><svg width="10" height="10" viewBox="0 0 10 10"><path d="M2 1l7 4-7 4z" fill="#fff"/></svg></span></div>
  <div class="abs stats">
    <div class="stat"><b>120<span>+</span></b><small>Project Complete</small></div>
    <div class="stat"><b>98<span>%</span></b><small>Client Satisfaction</small></div>
  </div>
  <div class="abs quote-txt">Get Your Construction Quote Today!</div>
  <div class="abs quote-go"><svg width="12" height="12" viewBox="0 0 12 12"><path d="M4 2l4 4-4 4" stroke="#fff" stroke-width="1.6" fill="none"/></svg></div>
</section>

<section class="about">
  <p class="abs para">Kestrim is a Service-Disabled Veteran-Owned Small Business (SDVOSB) providing excellence in general contracting, design-build construction, disaster recovery, and environmental remediation. With years of expertise, we proudly serve federal, state, and local agencies along with hospitals and schools.</p>
  <div class="abs link">ABOUT US <span class="dot-gold"></span></div>
  <h2 class="abs">Building with<br>Integrity, Precision,<br>and Vision</h2>
  <div class="abs team-photo" role="img" aria-label="Three contractors in hard hats reviewing plans on site"></div>
  <div class="abs features">
    <div class="feature"><div class="head"><span class="badge"></span><h3>Experience<br>You Can Trust</h3></div><p>Lorem ipsum dolor sit consectetur adipiscing elit ut elit tellus luctu nec ullamcorper mattis pulvinar.</p></div>
    <div class="feature"><div class="head"><span class="badge"></span><h3>Highest<br>Safety First</h3></div><p>Lorem ipsum dolor sit consectetur adipiscing elit ut elit tellus luctu nec ullamcorper mattis pulvinar.</p></div>
    <div class="feature"><div class="head"><span class="badge"></span><h3>Innovative<br>Solutions</h3></div><p>Lorem ipsum dolor sit consectetur adipiscing elit ut elit tellus luctu nec ullamcorper mattis pulvinar.</p></div>
  </div>
</section>

<section class="services">
  <svg class="abs" style="left:0;top:0" width="1200" height="653" viewBox="0 0 1200 653" preserveAspectRatio="none">
    <path d="M0 18H600C625 18 630 0 655 0H1200V635H600C575 635 570 653 545 653H0z" fill="#0e0e0e"/>
  </svg>
  <h2 class="abs">Professional Construction<br>&amp; Contracting Services</h2>
  <p class="abs sub">Comprehensive solutions tailored for mission-critical infrastructure.</p>
  <ul class="abs svc-list">
    <li>General Contracting</li>
    <li class="active">Design-Build Construction<small>Innovative, cost-effective construction delivery.</small></li>
    <li>Disaster Recovery</li>
    <li>Environmental Remediation</li>
  </ul>
  <div class="abs pill"><span class="avatar" role="img" aria-label="Contractor portrait"></span>GET YOUR CONSTRUCTION<br>QUOTE TODAY!<span class="dot-gold"></span></div>
  <div class="abs svc-photo" role="img" aria-label="Two contractors reviewing blueprints"></div>
</section>

<section class="industries">
  <h2 class="abs">Industries We Serve<br>Proudly Serving</h2>
  <p class="abs intro">We take pride in delivering construction projects that stand strong for generations. Explore some of our featured works below.</p>
  <div class="abs link">VIEW ALL INDUSTRY <span class="dot-gold"></span></div>
  <div class="abs tile t1" role="img" aria-label="Aerial view of a federal defense campus"><div class="cap"><small>Industry</small><b>KZE Federal Division</b></div><span class="go"></span></div>
  <div class="abs tile t2" role="img" aria-label="State capitol building"></div>
  <div class="abs tile t3" role="img" aria-label="Modern hospital building with green walls"></div>
  <div class="abs tile t4" role="img" aria-label="Historic university campus"></div>
</section>

<section class="values">
  <svg class="abs" style="left:0;top:0" width="1200" height="288" viewBox="0 0 1200 288" preserveAspectRatio="none">
    <defs><linearGradient id="gv" x1="0" x2="1"><stop offset="0" stop-color="#b88a2c"/><stop offset=".5" stop-color="#e6cb62"/><stop offset="1" stop-color="#bf9031"/></linearGradient></defs>
    <path d="M0 0H355C375 0 380 18 400 18H1200V288H0z" fill="url(#gv)"/>
  </svg>
  <div class="value" style="left:126px"><div class="circ"><span></span></div>Veteran Owned<br>SDVOSB Certified</div>
  <div class="value" style="left:366px"><div class="circ"><span></span></div>Proven Experience in<br>Government Projects</div>
  <div class="value" style="left:619px"><div class="circ"><span></span></div>Quality, Safety &amp;<br>Compliance First</div>
  <div class="value" style="left:850px"><div class="circ"><span></span></div>Timely Delivery &amp;<br>Cost Efficiency</div>
</section>

<section class="contact">
  <div class="abs c-card">
    <h2>Let’s Build<br>Your Vision</h2>
    <div class="tag">“Have a Vision? We Build It Together.”</div>
    <p>Have a question about our construction services, pricing, or ongoing projects?</p>
    <ul>
      <li><svg class="ico" viewBox="0 0 10 10"><path d="M2 0l2 2-1 1.5a6 6 0 0 0 3.5 3.5L8 6l2 2-1.5 2C4 10 0 6 0 1.5z"/></svg>+1 (234) 567 890</li>
      <li><svg class="ico" viewBox="0 0 10 10"><path d="M5 0a3.5 3.5 0 0 0-3.5 3.5C1.5 6 5 10 5 10s3.5-4 3.5-6.5A3.5 3.5 0 0 0 5 0z"/></svg>123 Main Street, City, Country</li>
      <li><svg class="ico" viewBox="0 0 10 10"><path d="M0 2h10v6H0z"/></svg>info@yourcompany.com</li>
    </ul>
  </div>
  <div class="abs form">
    <h3>Let’s Turn Your <span>Construction</span><br>Ideas into Reality.</h3>
    <div class="fields">
      <div class="field">Full Name</div><div class="field">Email</div>
      <div class="field">Phone Number</div><div class="field">Service Interested in</div>
      <div class="field full">Message</div>
    </div>
    <span class="btn-gold">Send Message</span>
  </div>
</section>

<footer class="footer">
  <svg class="abs" style="left:0;top:-18px" width="1200" height="20" viewBox="0 0 1200 20" preserveAspectRatio="none"><path d="M600 20C625 20 630 0 655 0H1200V20z" fill="#151515"/></svg>
  <div class="brand"><span class="mark"></span>Kestrim</div>
  <div class="abs tag">Building Better Futures</div>
  <p class="abs about-f">We bring innovation and dedication to every project, helping clients achieve lasting results.</p>
  <div class="abs f-soc"><span><i></i></span><span><i></i></span><span><i></i></span><span><i></i></span></div>
  <div class="abs vline"></div>
  <div class="abs hline"></div>
  <div class="abs ready">Ready to start your<br>next project?</div>
  <span class="btn-gold">Get A Free Quote</span>
  <div class="abs cols">
    <div class="col"><h4>Top Links</h4><ul><li>Home</li><li>About Us</li><li>Services</li><li>Contact</li></ul></div>
    <div class="col"><h4>Explore</h4><ul><li>Projects</li><li>Blog</li><li>Careers</li><li>FAQ</li></ul></div>
    <div class="col"><h4>Resources</h4><ul><li>Privacy Policy</li><li>Terms &amp; Conditions</li><li>Help Center</li><li>Support</li></ul></div>
  </div>
  <div class="abs bottom"><span>Terms &amp; Condition</span><span>© 2025 Kestrim. All rights reserved.</span><span>Privacy Policy</span></div>
</footer>

</body>
</html>
```